Producer Needs a Movie Poster for a Dramatic Film

We need a movie poster for a new dramatic film called "Dust Over Morning".
Synopisis: A young drug addict (cocaine and alcohol), REED MORROW, has hit rock bottom after a continuous downward spiral of alcoholism and drug abuse, leaving him with nothing to live for. His ex-girlfriend left him. His best friend doesn’t want anything to do with him. Unable to rehabilitate himself after multiple attempts, he attempts suicide (Jumping off of a high-rise apartment building).
We want the poster to give the dark feel of the film. It should be serious and personable.
We want the three lead actors to be listed on the top of the poster from left to right (Gerald Pinsk, Corinne Velasq, Darek Ombuvia).
The title of the film, Dust Over Morning, should be in the center of the poster.
We want "Coming Soon" centered on the bottom of the poster.

No pictures will be provided for this poster, so be creative and make something special for us to use. We're looking for a variety of good ideas.

We're excited to see what you come up with!

Please, make sure you provide us with files we can easily use. Also, we would like a copy of the film title in a separate file for easy use as well. So, two files total (One with the poster, One with just the film title by itself).

Industry/Entity Type

Movie

Requirements
Must have
• We want the three lead actors to be listed on the top of the poster from left to right (Gerald Pinsk, Corinne Velasq, Darek Ombuvia).
• The title of the film, Dust Over Morning, should be in the center of the poster.
• We want "Coming Soon" centered on the bottom of the poster.
• Please, make sure you provide us with files we can easily use. Also, we would like a copy of the film title in a separate file for easy use as well. So, two files total (One with the poster, One with just the film title by itself).
Should not have
• Should not have a person on the poster unless they are unrecognizable and you can't see any characteristics. We can't have someone on the poster who won't be in the movie.
• Don't put each locations that won't be in the film either. It takes place in LOs Angeles. Mostly on a high-rise apartment building rooftop.

```html
<!DOCTYPE html>
<html lang="en">
<head>
<meta charset="utf-8">
<title>Dust Over Morning — Poster</title>
<link rel="stylesheet" href="https://fonts.googleapis.com/css2?family=Josefin+Sans:wght@300;400&family=Oswald:wght@700&display=swap">
<style>
  :root {
    --page: #ffffff;
    --poster: #000000;
    --credit: #cfcfcf;
    --tagline: #bdbdbd;
    --rule: #8a8a8a;
  }
  html, body {
    margin: 0;
    padding: 0;
    width: 900px;
    height: 1200px;
    overflow: hidden;
    background: var(--page);
  }
  .canvas {
    position: relative;
    width: 900px;
    height: 1200px;
    background: var(--page);
  }
  .poster {
    position: absolute;
    left: 146px;
    top: 170px;
    width: 607px;
    height: 858px;
    background: var(--poster);
    overflow: hidden;
  }
  .cast {
    position: absolute;
    top: 48px;
    left: 0;
    width: 100%;
    margin: 0;
    padding: 0;
    list-style: none;
  }
  .cast-member {
    position: absolute;
    width: 160px;
    text-align: center;
    font-family: "Josefin Sans", sans-serif;
    font-weight: 300;
    font-size: 15px;
    line-height: 18px;
    letter-spacing: 0;
    text-transform: uppercase;
    color: var(--credit);
  }
  .cast-member:nth-child(1) { left: 0px; }
  .cast-member:nth-child(2) { left: 222px; }
  .cast-member:nth-child(3) { left: 446px; }
  .title-art {
    position: absolute;
    left: 0;
    top: 0;
    width: 607px;
    height: 858px;
  }
  .release {
    position: absolute;
    left: 0;
    top: 780px;
    margin: 0;
    width: 100%;
    display: flex;
    justify-content: center;
    align-items: center;
    gap: 5px;
    font-family: "Josefin Sans", sans-serif;
    font-weight: 300;
    font-size: 15px;
    letter-spacing: 0.02em;
    text-transform: uppercase;
    color: var(--tagline);
  }
  .release-rule {
    display: block;
    width: 60px;
    height: 1px;
    background: var(--rule);
  }
</style>
</head>
<body>
<div class="canvas">
  <section class="poster">
    <ul class="cast">
      <li class="cast-member">Gerald<br>Pinsk</li>
      <li class="cast-member">Corinne<br>Velasq</li>
      <li class="cast-member">Darek<br>Ombuvia</li>
    </ul>

    <svg class="title-art" viewBox="0 0 607 858" role="img" aria-label="Film title Dust Over Morning, letters filled with a misty grey rooftop sky photograph showing a lone hooded silhouette, birds and a dark city edge">
      <defs>
        <linearGradient id="sky-base" gradientUnits="userSpaceOnUse" x1="90" y1="330" x2="540" y2="640">
          <stop offset="0" stop-color="#5a5a5a"/>
          <stop offset="0.25" stop-color="#a8a8a8"/>
          <stop offset="0.45" stop-color="#d9d9d9"/>
          <stop offset="0.6" stop-color="#b0b0b0"/>
          <stop offset="0.8" stop-color="#6a6a6a"/>
          <stop offset="1" stop-color="#2a2a2a"/>
        </linearGradient>
        <linearGradient id="sky-streak" gradientUnits="userSpaceOnUse" x1="100" y1="470" x2="560" y2="560">
          <stop offset="0" stop-color="#ffffff" stop-opacity="0"/>
          <stop offset="0.35" stop-color="#f4f4f4" stop-opacity="0.75"/>
          <stop offset="0.55" stop-color="#ffffff" stop-opacity="0.9"/>
          <stop offset="0.8" stop-color="#ffffff" stop-opacity="0.2"/>
          <stop offset="1" stop-color="#ffffff" stop-opacity="0"/>
        </linearGradient>
        <radialGradient id="sky-shadow" gradientUnits="userSpaceOnUse" cx="210" cy="560" r="80">
          <stop offset="0" stop-color="#000" stop-opacity="0.85"/>
          <stop offset="1" stop-color="#000" stop-opacity="0"/>
        </radialGradient>
        <linearGradient id="ground-fade" gradientUnits="userSpaceOnUse" x1="0" y1="500" x2="0" y2="630">
          <stop offset="0" stop-color="#000" stop-opacity="0"/>
          <stop offset="1" stop-color="#000" stop-opacity="0.75"/>
        </linearGradient>
        <g id="title-lettering" font-family="Oswald, sans-serif" font-weight="700">
          <text x="197" y="375" font-size="94" textLength="298" lengthAdjust="spacingAndGlyphs">DUST OVER</text>
          <text x="89" y="605" font-size="224" textLength="430" lengthAdjust="spacingAndGlyphs">MORNING</text>
        </g>
      </defs>
      <g class="film-title" transform="translate(0 40) skewY(-9)">
        <use href="#title-lettering" fill="url(#sky-base)"/>
        <use href="#title-lettering" fill="url(#sky-streak)" aria-hidden="true"/>
        <use href="#title-lettering" fill="url(#sky-shadow)" aria-hidden="true"/>
        <use href="#title-lettering" fill="url(#ground-fade)" aria-hidden="true"/>
      </g>
    </svg>

    <p class="release">
      <span class="release-rule"></span>
      <span class="release-text">Coming Soon</span>
      <span class="release-rule"></span>
    </p>
  </section>
</div>
</body>
</html>
```